Sponsor at Title Insurance Industry Seminar for Continuing Ed - 250 Companies in Attendance

I offer escrow accounting services in the Title Insurance Industry. I've attached logo files and an example of my former company. I don't like the design and it's a little wordy but it provides detail of what I offer.

Below is a brief write-up...
For professionals in the title insurance industry, finding a reliable and cost-effective solution to escrow accounting needs can feel overwhelming. When choosing the right accounting partner, title companies and law firms need a group they can trust, and that’s where we come in. Brightfen Ledger Works is a team that understands the title industry and the importance of compliance, security and accuracy. Brightfen Ledger Works is the experienced, convenient and cost-effective choice for the accounting and certification needs of companies throughout the country.

```html
<!DOCTYPE html>
<html lang="en">
<head>
<meta charset="utf-8">
<title>Brightfen Ledger Works – Escrow Reconciliation Services</title>
<link href="https://fonts.googleapis.com/css2?family=Montserrat:wght@500;600;700&family=Lato:ital,wght@0,400;0,700;1,400;1,700&display=swap" rel="stylesheet">
<style>
:root{
  --copper:#b8664b;
  --copper-light:#dc9c82;
  --copper-pale:#f0c9b8;
  --slate:#323b47;
  --slate-soft:#4a5461;
  --ink:#2a2e35;
  --paper:#ffffff;
  --backdrop:#e9e7e4;
}
*{box-sizing:border-box;margin:0;padding:0}
html,body{width:1200px;height:1200px;overflow:hidden;background:var(--backdrop)}
body{position:relative;font-family:"Lato",sans-serif;color:var(--ink)}
.page{position:absolute;top:225px;width:570px;height:750px;background:var(--paper);overflow:hidden;box-shadow:0 6px 20px rgba(0,0,0,.12)}
.page--front{left:20px}
.page--back{left:610px}
.abs{position:absolute}

/* brand */
.brand{display:flex;align-items:center;gap:10px}
.brand__mark{width:34px;height:34px;background:var(--copper);border-radius:50%}
.brand__name{font-family:"Montserrat",sans-serif;font-weight:600;color:var(--copper);font-size:24px;line-height:1.05;letter-spacing:.5px;text-transform:uppercase}

.rule{height:5px;background:repeating-linear-gradient(90deg,var(--copper-light) 0 1px,transparent 1px 3px)}

/* front */
.hero-photo{left:35px;top:50px;width:270px;height:340px;border:2px solid var(--copper-pale);border-radius:0 90px 0 90px;overflow:hidden}
.hero-photo__fill{position:absolute;inset:6px;border-radius:0 84px 0 84px;background:linear-gradient(135deg,#c7ccd3,#e9edf1 45%,#6f7884)}
.hero-photo__accent{left:65px;top:50px;width:130px;height:120px;background:var(--copper);border-radius:0 40px 0 0;opacity:.85}
.title{right:45px;top:130px;text-align:right;font-family:"Montserrat",sans-serif;font-weight:600;font-size:29px;line-height:1.15;color:var(--ink)}
.title .accent{color:var(--copper)}
.intro{left:325px;top:255px;width:200px;font-size:8px;line-height:1.38;text-align:justify;text-align-last:right}
.cta-band{left:40px;top:400px;width:500px;height:52px;background:linear-gradient(90deg,var(--copper) 0%,var(--copper-light) 100%);color:#fff;font-style:italic;font-weight:700;font-size:9.5px;text-align:center;display:flex;align-items:center;justify-content:center;padding:0 40px;line-height:1.4}
.features{left:58px;top:480px;display:flex;gap:8px}
.feature{width:105px;height:82px;background:linear-gradient(160deg,var(--slate-soft),var(--slate));border-radius:8px;color:#e7e9ec;font-size:7.5px;text-align:center;display:flex;flex-direction:column;align-items:center;justify-content:flex-end;padding:0 6px 9px;gap:6px;line-height:1.25}
.feature svg{width:36px;height:32px}
.closing{left:40px;top:600px;width:290px;font-family:"Montserrat",sans-serif;font-weight:500;font-size:22px;line-height:1.3;color:var(--copper-light)}
.desk-photo{right:45px;top:595px;width:135px;height:120px;border-radius:0 0 0 40px;background:linear-gradient(150deg,#8a939e,#dfe5ec 55%,#a8c3dc)}
.footer{left:0;bottom:0;width:100%;height:40px;background:var(--slate);display:flex;align-items:center;gap:14px;padding-left:28px;color:#fff;font-style:italic;font-weight:700;font-size:9.5px}
.contact{display:flex;align-items:center;gap:5px}
.contact__dot{width:14px;height:14px;border-radius:50%;background:var(--copper-light);display:flex;align-items:center;justify-content:center}
.contact__dot svg{width:8px;height:8px}

/* back */
.back-brand{left:28px;top:50px}
.portrait{right:0;top:0;width:330px;height:370px;background:linear-gradient(200deg,#eef1f4,#c9d0d8 50%,#7d6b5c 85%,#d8c5ad)}
.services{left:25px;top:145px;width:225px;height:225px;background:#fff;border:2px solid var(--copper-light);padding:10px 14px}
.services__title{font-family:"Montserrat",sans-serif;font-weight:700;font-size:18px;text-align:center;color:var(--slate);margin-bottom:6px}
.service{display:flex;align-items:center;gap:14px;height:58px;font-size:12.5px;color:var(--slate-soft);line-height:1.2}
.service + .service{border-top:4px solid transparent;border-image:repeating-linear-gradient(90deg,var(--copper-pale) 0 1px,transparent 1px 3px) 4}
.service svg{width:32px;height:32px;flex:none}
.work-photo{left:0;top:370px;width:300px;height:230px;background:linear-gradient(120deg,#51606f,#bccbd8 45%,#f5f7f9)}
.who{right:40px;top:400px;width:280px;text-align:right}
.who__title{font-family:"Montserrat",sans-serif;font-weight:700;font-size:18px;color:var(--copper);margin-bottom:12px}
.who__text{font-size:11px;line-height:1.45;margin-bottom:12px}
.who__tag{font-style:italic;font-weight:700;font-size:12px;color:var(--copper);line-height:1.4}
.stats-band{left:0;top:620px;width:100%;height:72px;background:linear-gradient(90deg,var(--copper-light),var(--copper))}
.stats-photo{left:10px;top:610px;width:150px;height:100px;border-radius:0 0 0 35px;background:linear-gradient(150deg,#8a939e,#dfe5ec 55%,#a8c3dc)}
.stats{left:185px;top:628px;width:360px;color:#fff}
.stats__lead{font-size:7.5px;line-height:1.3;margin-bottom:8px}
.stats__row{display:flex}
.stat{flex:1;text-align:center;font-family:"Lato",sans-serif;font-weight:700;line-height:1.05}
.stat + .stat{border-left:1px solid rgba(255,255,255,.6)}
.stat__num{font-size:15px}
.stat__label{font-size:10px}
.page--back .footer{justify-content:flex-end;padding-right:30px;font-size:8.5px}
</style>
</head>
<body>

<!-- Front page -->
<section class="page page--front">
  <div class="abs hero-photo"><div class="hero-photo__fill" role="img" aria-label="Photo of a man working on a laptop at a high table by an office window"></div></div>
  <div class="abs hero-photo__accent"></div>

  <div class="abs brand" style="right:45px;top:40px">
    <span class="brand__mark"></span>
    <span class="brand__name">Brightfen<br>Ledger Works</span>
  </div>
  <div class="abs rule" style="left:325px;top:112px;width:200px"></div>

  <h1 class="abs title"><span class="accent">Escrow</span><br>Reconciliation<br>Services</h1>
  <div class="abs rule" style="left:325px;top:243px;width:200px"></div>

  <p class="abs intro">For professionals in the title insurance industry, finding a reliable &amp; cost-effective solution to escrow accounting needs can feel overwhelming. When choosing the right accounting partner, title companies and law firms need a group they can trust, &amp; that's where we come in. Brightfen Ledger Works is a team that understands the title industry and the importance of compliance, security &amp; accuracy. Brightfen Ledger Works is the experienced, convenient and cost-effective choice for the accounting and certification needs of companies throughout the country.</p>

  <div class="abs cta-band">Since every office operates differently, contact us today for an individualized rate quote for escrow account reconciliation services!</div>

  <div class="abs features">
    <div class="feature">
      <svg viewBox="0 0 36 32" fill="none" stroke="var(--copper-light)" stroke-width="3.5" stroke-linecap="round" stroke-linejoin="round"><path d="M6 14v-3a4 4 0 0 1 4-4h20M25 2l5 5-5 5"/><path d="M30 18v3a4 4 0 0 1-4 4H6M11 20l-5 5 5 5"/></svg>
      <span>Daily<br>two-way reconciling</span>
    </div>
    <div class="feature">
      <svg viewBox="0 0 36 32" fill="none" stroke="var(--copper-light)" stroke-width="2"><rect x="3" y="4" width="30" height="19" rx="1"/><path d="M14 28h8M18 23v5M9 17l6-6 4 4 7-7"/></svg>
      <span>Regardless of your<br>accounting software system</span>
    </div>
    <div class="feature">
      <svg viewBox="0 0 36 32" fill="var(--copper-light)"><rect x="4" y="20" width="5" height="9"/><rect x="12" y="15" width="5" height="14"/><rect x="20" y="17" width="5" height="12"/><rect x="28" y="10" width="5" height="19"/><path d="M3 16l9-8 6 5 12-10" fill="none" stroke="var(--copper-light)" stroke-width="2.5"/></svg>
      <span>Comprehensive daily<br>and monthly reports</span>
    </div>
    <div class="feature">
      <svg viewBox="0 0 36 32" fill="none" stroke="var(--copper-light)" stroke-width="2"><rect x="3" y="9" width="30" height="16" rx="1"/><circle cx="18" cy="17" r="5"/><path d="M6 6h26"/></svg>
      <span>low, affordable<br>rates</span>
    </div>
  </div>

  <p class="abs closing">Our team of experienced professionals can be your perfect solution!</p>
  <div class="abs desk-photo" role="img" aria-label="Photo of hands typing on a laptop beside printed charts"></div>

  <footer class="abs footer">
    <span class="contact"><span class="contact__dot"><svg viewBox="0 0 8 8" fill="none" stroke="#fff" stroke-width="1"><circle cx="4" cy="4" r="3"/><path d="M1 4h6M4 1v6"/></svg></span>www.brightfenledger.com</span>
    <span class="contact"><span class="contact__dot"><svg viewBox="0 0 8 8" fill="none" stroke="#fff" stroke-width="1"><rect x="1" y="2" width="6" height="4"/><path d="M1 2l3 2 3-2"/></svg></span>info@brightfenledger.com</span>
    <span class="contact"><span class="contact__dot"><svg viewBox="0 0 8 8" fill="#fff"><path d="M2 1l1.3 1.7-.7.8a4 4 0 0 0 1.9 1.9l.8-.7L7 6l-.8 1C3.5 7 1 4.5 1 1.8z"/></svg></span>(555) 014-2290</span>
  </footer>
</section>

<!-- Back page -->
<section class="page page--back">
  <div class="abs portrait" role="img" aria-label="Photo of a smiling businesswoman at a desk with documents and a calculator"></div>

  <div class="abs brand back-brand">
    <span class="brand__mark"></span>
    <span class="brand__name">Brightfen<br>Ledger Works</span>
  </div>

  <div class="abs services">
    <h2 class="services__title">OUR SERVICES</h2>
    <div class="service">
      <svg viewBox="0 0 32 32" fill="none" stroke="var(--copper)" stroke-width="2"><rect x="6" y="4" width="20" height="24" rx="1"/><path d="M10 11h12M10 16h12M10 21h8"/></svg>
      <span>Escrow Reconciliation<br>Services</span>
    </div>
    <div class="service">
      <svg viewBox="0 0 32 32" fill="var(--copper-light)" stroke="var(--copper)" stroke-width="1.5"><path d="M16 3l11 4v9c0 7-5 11-11 13C10 27 5 23 5 16V7z"/></svg>
      <span>NTLA Best Practice<br>Certification</span>
    </div>
    <div class="service">
      <svg viewBox="0 0 32 32" fill="none" stroke="var(--copper)" stroke-width="2.5"><circle cx="16" cy="12" r="4"/><path d="M16 3v3M16 18v3M7 12h3M22 12h3M10 6l2 2M20 16l2 2M22 6l-2 2M12 16l-2 2"/><path d="M4 26c4 0 6-3 10-3h6l-2 3h-5" stroke-width="2"/></svg>
      <span>Other Related<br>Services</span>
    </div>
  </div>

  <div class="abs work-photo" role="img" aria-label="Photo of a hand writing on financial papers next to a calculator"></div>

  <div class="abs who">
    <h2 class="who__title">WHO WE ARE</h2>
    <p class="who__text">Harrowgate Accounting Service is a team of accounting experts who understand the title world – and the importance of compliance, security and up-to-date books within it.</p>
    <p class="who__tag">Our team of experienced professionals can be your perfect solution!</p>
  </div>

  <div class="abs stats-band"></div>
  <div class="abs stats-photo" role="img" aria-label="Photo of hands typing on a laptop beside printed charts"></div>
  <div class="abs stats">
    <p class="stats__lead">Put Harrowgate's knowledge and experience to work for you. We want to help you achieve:</p>
    <div class="stats__row">
      <div class="stat"><div class="stat__num">100%</div><div class="stat__label">COMPLIANCE</div></div>
      <div class="stat"><div class="stat__num">100%</div><div class="stat__label">CONVENIENCE</div></div>
      <div class="stat"><div class="stat__num">100%</div><div class="stat__label">CREDIBILITY</div></div>
    </div>
  </div>

  <footer class="abs footer">
    <span class="contact"><span class="contact__dot"><svg viewBox="0 0 8 8" fill="none" stroke="#fff" stroke-width="1"><circle cx="4" cy="4" r="3"/><path d="M1 4h6M4 1v6"/></svg></span>www.brightfenledger.com</span>
    <span class="contact"><span class="contact__dot"><svg viewBox="0 0 8 8" fill="none" stroke="#fff" stroke-width="1"><rect x="1" y="2" width="6" height="4"/><path d="M1 2l3 2 3-2"/></svg></span>info@brightfenledger.com</span>
    <span class="contact"><span class="contact__dot"><svg viewBox="0 0 8 8" fill="#fff"><path d="M2 1l1.3 1.7-.7.8a4 4 0 0 0 1.9 1.9l.8-.7L7 6l-.8 1C3.5 7 1 4.5 1 1.8z"/></svg></span>(555) 014-2290</span>
  </footer>
</section>

</body>
</html>
```